Zielgruppe
Hypnose
Aufgabenstellung
Text Vorder- und Rückseite siehe Anlage
Auf der Vorderseite Foto und Logo (auch in der Anlage)
Farbgestaltung passend zu den Logofarben
Das Design soll kreativ und freundlich sein

```html
<!DOCTYPE html>
<html lang="de">
<head>
<meta charset="utf-8">
<title>stillwerk Hypnose – Flyer</title>
<link href="https://fonts.googleapis.com/css2?family=Montserrat:wght@400;500;700&display=swap" rel="stylesheet">
<style>
  :root {
    --orange: #e8532b;
    --blush: #fbdcdb;
    --white: #ffffff;
    --ink: #333333;
    --backdrop: #d6d6d6;
    --photo-a: #c9b4a4;
    --photo-b: #f2c2b6;
  }
  * { box-sizing: border-box; margin: 0; padding: 0; }
  html, body { width: 1059px; height: 1200px; overflow: hidden; }
  body {
    background: var(--backdrop);
    font-family: "Montserrat", sans-serif;
    color: var(--ink);
    position: relative;
  }
  .card {
    position: absolute;
    width: 441px;
    height: 881px;
    background: var(--white);
    overflow: hidden;
  }
  .card--front { left: 73px; top: 105px; }
  .card--back { left: 555px; top: 217px; }
  .card__shape { position: absolute; left: 0; top: 0; }

  /* Front */
  .brand {
    position: absolute; left: 0; right: 0; top: 178px;
    text-align: center;
  }
  .brand__mark {
    display: block; width: 70px; height: 70px; border-radius: 50%;
    background: var(--blush); margin: -100px auto 26px;
  }
  .brand__name {
    color: var(--orange); font-weight: 500; font-size: 30px; letter-spacing: 1px;
  }
  .portrait {
    position: absolute; left: 127px; top: 277px;
    width: 198px; height: 198px; border-radius: 50%;
    border: 8px solid var(--white);
    background: radial-gradient(circle at 50% 40%, var(--photo-b), var(--photo-a));
  }
  .person { position: absolute; left: 48px; top: 468px; color: var(--white); }
  .person__title { font-size: 24px; font-weight: 500; line-height: 30px; }
  .person__name { font-size: 25px; font-weight: 700; line-height: 30px; }
  .person__degree { font-size: 18px; margin-top: 8px; }
  .contact { position: absolute; left: 48px; top: 596px; list-style: none; }
  .contact__item {
    display: flex; align-items: flex-start; color: var(--white);
    font-size: 18px; line-height: 24px; height: 40px;
  }
  .contact__icon {
    flex: none; width: 32px; height: 32px; border-radius: 50%;
    background: var(--blush); margin-right: 17px; margin-top: -4px;
    display: flex; align-items: center; justify-content: center;
  }
  .card__footer {
    position: absolute; left: 0; right: 0; bottom: 0; height: 69px;
    background: var(--blush); display: flex; align-items: center; justify-content: center;
    font-size: 17px; color: var(--ink);
  }

  /* Back */
  .section { position: absolute; left: 53px; right: 40px; }
  .section__title { font-size: 17.5px; font-weight: 700; color: var(--orange); }
  .section__rule { width: 41px; height: 3px; background: var(--orange); margin: 9px 0 14px; }
  .section__text { font-size: 14.3px; line-height: 20.7px; }
  .benefits { list-style: none; margin-top: 33px; }
  .benefits li { font-size: 14.8px; line-height: 23.6px; display: flex; align-items: center; }
  .benefits svg { margin-right: 19px; flex: none; }
  .section--about { top: 600px; }
  .section--about .section__title { color: var(--white); }
  .section--about .section__rule { background: var(--white); }
  .section--about .section__text { color: #fde3df; }
  .section--about strong { color: var(--white); }
</style>
</head>
<body>

<section class="card card--front">
  <svg class="card__shape" width="441" height="812" viewBox="0 0 441 812" aria-hidden="true">
    <path d="M0,385 C70,362 140,352 226,356 C320,362 390,385 441,411 V812 H0 Z" fill="var(--orange)"/>
  </svg>
  <div class="brand">
    <span class="brand__mark"></span>
    <span class="brand__name">stillwerk Hypnose</span>
  </div>
  <div class="portrait" role="img" aria-label="Porträtfoto der Hypnosetherapeutin"></div>
  <div class="person">
    <p class="person__title">Mag.</p>
    <p class="person__name">Lena Kelbrinos</p>
    <p class="person__degree">B.Ed, M.Sc</p>
  </div>
  <ul class="contact">
    <li class="contact__item"><span class="contact__icon"><svg width="16" height="16" viewBox="0 0 24 24" fill="none" stroke="var(--orange)" stroke-width="2"><path d="M5 3h4l2 5-3 2a12 12 0 0 0 6 6l2-3 5 2v4a2 2 0 0 1-2 2A18 18 0 0 1 3 5a2 2 0 0 1 2-2z"/></svg></span>0660 48 213 90</li>
    <li class="contact__item"><span class="contact__icon"><svg width="16" height="16" viewBox="0 0 24 24" fill="none" stroke="var(--orange)" stroke-width="2"><rect x="3" y="5" width="18" height="14" rx="1"/><path d="M7 10l5 4 5-4"/></svg></span>hallo@stillwerk-hypnose.at</li>
    <li class="contact__item"><span class="contact__icon"><svg width="16" height="16" viewBox="0 0 24 24" fill="none" stroke="var(--orange)" stroke-width="2"><circle cx="12" cy="12" r="9"/><path d="M3 12h18M12 3c3 3 3 15 0 18M12 3c-3 3-3 15 0 18"/></svg></span>www.stillwerk-hypnose.at</li>
    <li class="contact__item"><span class="contact__icon"><svg width="16" height="16" viewBox="0 0 24 24" fill="none" stroke="var(--orange)" stroke-width="2"><path d="M12 21s-6-6-6-11a6 6 0 0 1 12 0c0 5-6 11-6 11z"/><circle cx="12" cy="10" r="2"/></svg></span>Am Lindenhang 14<br>2371 Hofwiesen</li>
  </ul>
  <footer class="card__footer">Sie brauchen nicht daran zu glauben, …</footer>
</section>

<section class="card card--back">
  <svg class="card__shape" width="441" height="812" viewBox="0 0 441 812" aria-hidden="true">
    <rect x="10" y="10" width="421" height="600" fill="var(--blush)"/>
    <path d="M0,570 C120,512 300,510 441,567 V812 H0 Z" fill="var(--white)"/>
    <path d="M0,580 C120,522 300,520 441,577 V812 H0 Z" fill="var(--orange)"/>
  </svg>
  <div class="section" style="top:40px;">
    <h2 class="section__title">Wie Hypnose Ihr Leben verändert</h2>
    <div class="section__rule"></div>
    <p class="section__text">Hypnose ist eine wunderbare Möglichkeit,<br>das eigene Leben zu verbessern.<br>Die Anwendungsbereiche sind unglaublich<br>vielfältig – wenn einer der folgenden Punkte<br>auf Sie zutrifft, sind Sie bei mir richtig:</p>
    <ul class="benefits">
      <li><svg width="18" height="10" viewBox="0 0 18 10" fill="none" stroke="var(--orange)" stroke-width="1.5"><path d="M0 5h17M12 1l5 4-5 4"/></svg>Wunsch mit dem Rauchen aufzuhören</li>
      <li><svg width="18" height="10" viewBox="0 0 18 10" fill="none" stroke="var(--orange)" stroke-width="1.5"><path d="M0 5h17M12 1l5 4-5 4"/></svg>Wunsch abzunehmen</li>
      <li><svg width="18" height="10" viewBox="0 0 18 10" fill="none" stroke="var(--orange)" stroke-width="1.5"><path d="M0 5h17M12 1l5 4-5 4"/></svg>Selbstvertrauen steigern</li>
      <li><svg width="18" height="10" viewBox="0 0 18 10" fill="none" stroke="var(--orange)" stroke-width="1.5"><path d="M0 5h17M12 1l5 4-5 4"/></svg>Prüfungsangst/Lernblockaden</li>
      <li><svg width="18" height="10" viewBox="0 0 18 10" fill="none" stroke="var(--orange)" stroke-width="1.5"><path d="M0 5h17M12 1l5 4-5 4"/></svg>Platzangst</li>
      <li><svg width="18" height="10" viewBox="0 0 18 10" fill="none" stroke="var(--orange)" stroke-width="1.5"><path d="M0 5h17M12 1l5 4-5 4"/></svg>Erschöpfung/Überforderung</li>
      <li><svg width="18" height="10" viewBox="0 0 18 10" fill="none" stroke="var(--orange)" stroke-width="1.5"><path d="M0 5h17M12 1l5 4-5 4"/></svg>Trauer/Frust</li>
      <li><svg width="18" height="10" viewBox="0 0 18 10" fill="none" stroke="var(--orange)" stroke-width="1.5"><path d="M0 5h17M12 1l5 4-5 4"/></svg>Wohlbefinden steigern</li>
      <li><svg width="18" height="10" viewBox="0 0 18 10" fill="none" stroke="var(--orange)" stroke-width="1.5"><path d="M0 5h17M12 1l5 4-5 4"/></svg>Schlafstörungen</li>
      <li><svg width="18" height="10" viewBox="0 0 18 10" fill="none" stroke="var(--orange)" stroke-width="1.5"><path d="M0 5h17M12 1l5 4-5 4"/></svg>Höhenangst/ Flugangst</li>
      <li><svg width="18" height="10" viewBox="0 0 18 10" fill="none" stroke="var(--orange)" stroke-width="1.5"><path d="M0 5h17M12 1l5 4-5 4"/></svg>Lampenfieber</li>
      <li><svg width="18" height="10" viewBox="0 0 18 10" fill="none" stroke="var(--orange)" stroke-width="1.5"><path d="M0 5h17M12 1l5 4-5 4"/></svg>Unsicherheit in Menschenmengen</li>
    </ul>
  </div>
  <div class="section section--about">
    <h2 class="section__title">Was ist Hypnose?</h2>
    <div class="section__rule"></div>
    <p class="section__text">Hypnose ist ein <strong>Zustand tiefer Entspannung</strong><br>der genutzt werden kann, um erwünschte<br>Gewohnheiten und Handlungsmuster zu<br>verstärken oder unerwünschte aufzulösen.<br>Zusätzlich ist Hypnose hervorragend geeig-<br>net, bei Stress oder Überforderung für <strong>innere<br>Ruhe und Wohlbefinden</strong> zu sorgen.</p>
  </div>
  <footer class="card__footer">… Sie brauchen es nur&nbsp;<strong>zuzulassen</strong>.</footer>
</section>

</body>
</html>
```